The Gemstone Craft Studio Sales Business Card

The goal of this project is to create a interactive & effective business card design for SALES purposes with the intention to get customer on to our website and make a purchase or contact us about a product or service.
Website: WWW.RINGFORGEHUB.COM
LocalBusinessPage: https://my.listing/RingForgeHUB?gm
Facebook & Instagram: @THEGEMSTONECRAFTSTUDIO
Phone # & Text Message & QuickChat Message: +1(555) 418-0293
Email: HELLO@RINGFORGEHUB.COM
Location: 4872 Brambleton Avenue Suite 512 Hollisbrook, NJ
(It would be necessary to have the appropriate ticker/icon for each social media platform as well as the location ticker and phone / messaging icons instead of spelling the words out.)
It is important to have the company logo and details but with an emphasis toward website. Feel free to also completely make one design your way and completely custom as you feel best.
The Gemstone Craft Studio is a Provider of Luxury Goods & Services such as: Custom Jewelry Design, Jewelry Repairs & Cleaning, Designer Jewelry, Luxury Gifts, 24 Karat Gold, 22 Karat Gold Jewelry, Diamond Jewelry, Insured Jewelry Appraisals, Loose Gemstones & Diamonds, Supporting Sustainability
Target Market(s)
People looking to invest in precious metals and gemstones as well as people looking to find a gift for a loved one for a special occasion. Customers looking to Custom Design Jewelry.
Contact Information for Business Card
Font styles to use
Other font styles liked:
- w.e you want
Colors
Designer to choose colors to be used in the design.
Requirements
Must have
- Website: WWW.RINGFORGEHUB.COM
- LocalBusinessPage: https://my.listing/RingForgeHUB?gm
- Facebook & Instagram: @THEGEMSTONECRAFTSTUDIO
- Phone # & Text Message & QuickChat Message: +1(555) 418-0293
- Email: HELLO@RINGFORGEHUB.COM
- Location: 4872 Brambleton Avenue Suite 512 Hollisbrook, NJ
- (It would be necessary to have the appropriate ticker/icon for each social media platform as well as the location ticker and phone / messaging icons instead of spelling the words out.)
- It is important to have the company logo and details but with an emphasis toward website. Feel free to also completely make one design your way and completely custom as you feel best.
Nice to have
- The Gemstone Craft Studio is a Provider of Luxury Goods & Services such as: Custom Jewelry Design, Jewelry Repairs & Cleaning, Designer Jewelry, Luxury Gifts, 24 Karat Gold, 22 Karat Gold Jewelry, Diamond Jewelry, Insured Jewelry Appraisals, Loose Gemstones & Diamonds, Supporting Sustainability

```html
<!DOCTYPE html>
<html lang="en">
<head>
<meta charset="utf-8">
<title>The Gemstone Craft Studio – Business Card</title>
<link rel="stylesheet" href="https://fonts.googleapis.com/css2?family=Alegreya:ital,wght@0,400;0,700;1,400&family=Roboto:ital,wght@1,400&display=swap">
<style>
  :root {
    --backdrop: #5e4e3b;
    --ink: #020203;
    --ink-soft: #08090c;
    --gold: #d9b36c;
    --red: #e21f2c;
    --serif: "Alegreya", Georgia, serif;
    --sans: "Roboto", Arial, sans-serif;
  }
  * { box-sizing: border-box; margin: 0; padding: 0; }
  html, body { width: 900px; height: 1200px; overflow: hidden; }
  body { background: var(--backdrop); position: relative; font-family: var(--serif); }

  .card {
    position: absolute; left: 75px; width: 768px; height: 439px;
    background: var(--ink); overflow: hidden;
  }
  .card--front { top: 133px; }
  .card--back { top: 627px; height: 441px; }
  .card__art { position: absolute; inset: 0; }

  /* Front */
  .listing { position: absolute; left: 0; right: 0; text-align: center; white-space: nowrap; }
  .listing__label { top: 120px; font-weight: 700; font-size: 26px; color: var(--red); letter-spacing: .5px; }
  .listing__url { top: 152px; font-style: italic; font-size: 27px; color: var(--gold); }
  .social-rule {
    position: absolute; top: 228px; left: 213px; width: 342px; height: 32px;
    display: flex; align-items: center; gap: 10px;
  }
  .social-rule__line { flex: 1; height: 2px; background: linear-gradient(90deg, transparent, var(--gold) 40%, var(--gold)); }
  .social-rule__line--end { background: linear-gradient(90deg, var(--gold), var(--gold) 60%, transparent); }
  .social-rule__dot { width: 32px; height: 32px; border-radius: 50%; background: var(--red); }
  .handle { top: 292px; font-size: 18px; letter-spacing: 3.6px; color: var(--gold); }

  /* Back */
  .glow {
    position: absolute; left: -30px; top: 0; width: 520px; height: 520px; border-radius: 50%;
    background: var(--ink-soft);
  }
  .brand { position: absolute; left: 40px; width: 360px; top: 92px; text-align: center; }
  .brand__mark { width: 72px; height: 72px; border-radius: 50%; background: var(--red); margin: 0 auto 100px; }
  .brand__name { font-size: 34px; line-height: 1.1; font-weight: 700; color: var(--red); letter-spacing: 1px; text-transform: uppercase; }

  .contact { position: absolute; left: 407px; top: 102px; width: 350px; color: var(--gold); }
  .contact__note { font-family: var(--sans); font-style: italic; font-size: 16px; line-height: 22px; margin-bottom: 36px; }
  .contact__list { list-style: none; }
  .contact__item { display: flex; align-items: flex-start; gap: 14px; font-size: 20px; line-height: 25px; margin-bottom: 22px; }
  .contact__item--phone { font-size: 22px; }
  .contact__item--web { letter-spacing: 1.6px; font-size: 17px; margin-bottom: 28px; }
  .contact__item--gap { margin-bottom: 16px; }
  .contact__icon { width: 24px; height: 24px; flex: none; fill: var(--red); margin-top: 1px; }
</style>
</head>
<body>

<section class="card card--front" aria-label="Card front">
  <svg class="card__art" viewBox="0 0 768 439">
    <defs>
      <linearGradient id="gem-tone" x1="0" y1="0" x2="1" y2="1">
        <stop offset="0" stop-color="#dcb874"/>
        <stop offset="1" stop-color="#c9a25e"/>
      </linearGradient>
    </defs>
    <polygon points="0,0 55,0 55,165 140,308 40,200 0,170" fill="var(--red)"/>
    <g role="img" aria-label="Faceted gem decoration, lower left corner">
      <polygon points="0,215 182,400 160,439 0,439" fill="url(#gem-tone)"/>
    </g>
    <g role="img" aria-label="Faceted gem decoration, upper right corner">
      <polygon points="588,42 625,0 768,0 768,250" fill="url(#gem-tone)"/>
    </g>
    <polygon points="632,132 715,262 768,262 768,439 715,439" fill="var(--red)"/>
  </svg>

  <p class="listing listing__label">LocalBusinessPage</p>
  <p class="listing listing__url">https://my.listing/RingForgeHUB?gm</p>
  <div class="social-rule" aria-label="Social profiles">
    <span class="social-rule__line"></span>
    <span class="social-rule__dot"></span>
    <span class="social-rule__dot"></span>
    <span class="social-rule__line social-rule__line--end"></span>
  </div>
  <p class="listing handle">@THEGEMSTONECRAFTSTUDIO</p>
</section>

<section class="card card--back" aria-label="Card back">
  <div class="glow"></div>

  <div class="brand">
    <div class="brand__mark"></div>
    <p class="brand__name">The Gemstone<br>Craft Studio</p>
  </div>

  <div class="contact">
    <p class="contact__note">Phone # &amp; Text Message<br>&amp; QuickChat Message</p>
    <ul class="contact__list">
      <li class="contact__item contact__item--phone">
        <svg class="contact__icon" viewBox="0 0 24 24" aria-hidden="true"><path d="M7 1h10a2 2 0 0 1 2 2v18a2 2 0 0 1-2 2H7a2 2 0 0 1-2-2V3a2 2 0 0 1 2-2zm0 3v14h10V4zm5 15.5a1.2 1.2 0 1 0 0 2.4 1.2 1.2 0 0 0 0-2.4z"/></svg>
        <span>+1(555) 418-0293</span>
      </li>
      <li class="contact__item contact__item--web">
        <svg class="contact__icon" viewBox="0 0 24 24" aria-hidden="true"><path d="M12 1a11 11 0 1 0 0 22 11 11 0 0 0 0-22zm-1 2.2V7H7.6A9 9 0 0 1 11 3.2zm2 0A9 9 0 0 1 16.4 7H13zM5.9 9H11v2H3.1a9 9 0 0 1 2.8-2zm7.1 0h5.1a9 9 0 0 1 2.8 2H13zM3.1 13H11v2H5.9a9 9 0 0 1-2.8-2zm9.9 0h7.9a9 9 0 0 1-2.8 2H13zm-5.4 4H11v3.8A9 9 0 0 1 7.6 17zm5.4 0h3.4a9 9 0 0 1-3.4 3.8z"/></svg>
        <span>WWW.RINGFORGEHUB.COM</span>
      </li>
      <li class="contact__item contact__item--gap">
        <svg class="contact__icon" viewBox="0 0 24 24" aria-hidden="true"><path d="M2 5h20v14H2zm2 2.2V17h16V7.2l-8 5.6z M4.5 7h15L12 12.2z"/></svg>
        <span>hello@ringforgehub.com</span>
      </li>
      <li class="contact__item">
        <svg class="contact__icon" viewBox="0 0 24 24" aria-hidden="true"><path d="M12 1a8 8 0 0 0-8 8c0 6 8 14 8 14s8-8 8-14a8 8 0 0 0-8-8zm0 11a3 3 0 1 1 0-6 3 3 0 0 1 0 6z"/></svg>
        <span>4872 Brambleton Avenue Suite,<br>512 Hollisbrook, NJ</span>
      </li>
    </ul>
  </div>
</section>

</body>
</html>
```